Marketing company needs business card design

Our company (Ventures Beyond Harbor) need a business card design for a marketing company. The design should of course include the logo and business colors (orange and blue). I would like the design to be clean and professional. The business card is going to be a die cut card that is leaf shaped (I have uploaded the template for it). I would love to see a design that is professional but nothing too "corporate."
Updates

Hello everyone,

Just wanted to let you know that I have uploaded an AI and EPS version of the logo for your convenience.

Thank you!

~Marlene

Industry/Entity Type

Marketing

Requirements
Must have
• Must have the following contact info:

Ventures Beyond Harbor
2817 Hollow Brook Ln B204
Prescott, AZ 86517

928.471.6083

info@venturesbeyondharbor-example.com

```html
<!DOCTYPE html>
<html lang="en">
<head>
<meta charset="utf-8">
<title>Ventures Beyond Harbor – Business Card</title>
<link rel="stylesheet" href="https://fonts.googleapis.com/css2?family=Arimo:wght@400;700&family=Noto+Serif:wght@700&display=swap">
<style>
  :root {
    --stage: #2b2b2b;
    --card-light: #ececec;
    --card-light-shade: #d6d6d6;
    --card-dark: #111111;
    --card-dark-shade: #1f1f1f;
    --brand-blue: #2a9fd6;
    --brand-orange: #f29a2e;
  }
  * { margin: 0; padding: 0; box-sizing: border-box; }
  html, body { width: 1200px; height: 900px; overflow: hidden; }
  body {
    background: var(--stage);
    font-family: "Arimo", Arial, sans-serif;
    position: relative;
  }
  .card {
    position: absolute;
    left: 355px;
    width: 490px;
    height: 280px;
    border-radius: 0 140px 0 140px;
    overflow: hidden;
  }
  .card--front { top: 150px; background: var(--card-light); }
  .card--back { top: 470px; background: var(--card-dark); }

  .card__texture {
    position: absolute;
    inset: 0;
  }
  .card--front .card__texture {
    background: radial-gradient(ellipse at 70% 30%, var(--card-light-shade), transparent 60%);
  }
  .card--back .card__texture {
    background: radial-gradient(ellipse at 25% 55%, var(--card-dark-shade), transparent 60%);
  }

  .brand-name {
    position: absolute;
    font-family: "Noto Serif", Georgia, serif;
    font-weight: 700;
    color: var(--brand-blue);
    line-height: 1.05;
  }
  .card--front .brand-name { left: 60px; top: 112px; font-size: 24px; width: 190px; }
  .card--back .brand-name { left: 215px; top: 86px; font-size: 26px; width: 230px; }

  .contact {
    position: absolute;
    left: 265px;
    top: 82px;
    list-style: none;
    color: var(--brand-blue);
    font-size: 11.5px;
    line-height: 1.35;
  }
  .contact__item { display: flex; gap: 7px; align-items: flex-start; margin-bottom: 12px; }
  .contact__item--tight { margin-bottom: 2px; }
  .contact__icon { width: 11px; height: 11px; flex: none; margin-top: 2px; }

  .website {
    position: absolute;
    left: 160px;
    top: 196px;
    color: var(--brand-blue);
    font-size: 13px;
    letter-spacing: 2px;
  }
</style>
</head>
<body>

<section class="card card--front">
  <div class="card__texture" role="img" aria-label="Faint pattern of scattered soft squares"></div>
  <p class="brand-name">Ventures Beyond Harbor</p>
  <ul class="contact">
    <li class="contact__item">
      <svg class="contact__icon" viewBox="0 0 12 12"><path d="M6 0.5a4 4 0 0 1 4 4c0 3-4 7-4 7s-4-4-4-7a4 4 0 0 1 4-4z" fill="var(--brand-orange)"/><circle cx="6" cy="4.5" r="1.5" fill="var(--card-light)"/></svg>
      <span>Ventures Beyond Harbor<br>2817 Hollow Brook Ln B204<br>Prescott, AZ 86517</span>
    </li>
    <li class="contact__item contact__item--tight">
      <svg class="contact__icon" viewBox="0 0 12 12"><rect x="1" y="1" width="10" height="10" rx="2" fill="var(--brand-orange)"/><path d="M4 3.5h4v5H4z" fill="var(--card-light)"/></svg>
      <span>928.471.6083</span>
    </li>
    <li class="contact__item">
      <svg class="contact__icon" viewBox="0 0 12 12"><rect x="0.5" y="2" width="11" height="8" rx="1" fill="var(--brand-orange)"/><path d="M1 2.5l5 4 5-4" fill="none" stroke="var(--card-light)" stroke-width="1"/></svg>
      <span>info@venturesbeyondharbor-example.com</span>
    </li>
  </ul>
</section>

<section class="card card--back">
  <div class="card__texture" role="img" aria-label="Faint pattern of scattered dark squares"></div>
  <p class="brand-name">Ventures Beyond Harbor</p>
  <p class="website">www.venturesbeyondharbor-example.com</p>
</section>

</body>
</html>
```